Dentist logo, business card and website

I have done an amateur job of creating a logo, business card and website. I would like it to look more professional. the current website can be found at www.tobenkarsh.com - I would like the website to be built and run through wix.com. The content on the website is as I would like it but I am open to suggestions.

The logo should be simple, may be best to keep to the letter TK - maybe to look like the V is a reflection of the A? Again, I am open to suggestions (I have attached a couple of images I have used on presentations but I would like the logo that you design to have a 'no fill' background so it can be placed on slides (for presentations etc).

The colour scheme seems wrong for a dentist, perhaps duck egg with black writing would be better? This applies to the business card as well (I have attached a PDF of some I have had made in the past but again they look amateur and colour scheme is wrong. The business cards should be landscape, have the logo in the top right corner, my name and qualifications in the middle, and my website and physical address in the bottom left corner: Glenmorrow Dental Surgery, 41-43 Pellow Crescent, Cardiff CF22 9RW.

Target Market(s)

30-60 year olds

Industry/Entity Type

Dental

Contact Information for Business Card

Please see brief and uploads.

Logo Text

TK

Number of Pages Required

4 page

Font styles to use
Decorative
Script

Requirements
Must have
• A sophisticated mature feel.
Nice to have
• Simplicity.
Should not have
• Anything too complicated.

```html
<!DOCTYPE html>
<html lang="en">
<head>
<meta charset="utf-8">
<title>Toben Karsh – Restorative &amp; Implant Dentist</title>
<link href="https://fonts.googleapis.com/css2?family=Cinzel:wght@400;700&family=Lato:ital,wght@0,400;0,700;1,400&display=swap" rel="stylesheet">
<style>
:root{
  --duck:#7fa3b1;
  --duck-dark:#6a909f;
  --ink:#2b2d33;
  --ink-soft:#333437;
  --text:#333;
  --muted:#888;
  --white:#fff;
  --teal-a:#2fa9a0;
  --teal-b:#0f6e99;
  --line:#d9d9d9;
}
*{box-sizing:border-box;margin:0;padding:0}
html,body{width:1200px;height:2190px;overflow:hidden;background:var(--white)}
body{position:relative;font-family:'Lato',sans-serif;color:var(--text)}
.abs{position:absolute}
a{color:inherit}

/* header */
.topline{left:0;top:0;width:1200px;height:4px;background:var(--ink)}
.top-email{right:308px;top:12px;font-size:15px;display:flex;align-items:center;gap:9px;white-space:nowrap}
.top-phone{left:912px;top:4px;width:208px;height:34px;background:var(--ink);color:var(--white);font-size:19px;display:flex;align-items:center;justify-content:center;gap:10px;border-radius:0 0 18px 18px}
.pill{top:58px;height:40px;border-radius:20px;background:var(--duck);color:var(--white);font-size:15px;display:flex;align-items:center;padding-left:58px;white-space:nowrap}
.pill .ic{position:absolute;left:0;top:-3px;width:46px;height:46px;border-radius:50%;background:var(--duck-dark);border:3px solid #fff;display:flex;align-items:center;justify-content:center}
.brand{left:95px;top:110px;width:230px;text-align:center;font-family:'Cinzel',serif;font-size:27px;color:var(--ink);letter-spacing:.5px;white-space:nowrap}
.nav{left:0;top:122px;width:1200px;height:51px;background:var(--duck)}
.nav-logo-tab{left:80px;top:122px;width:240px;height:38px;background:var(--white);border-radius:0 0 40px 40px}
.nav a{position:absolute;top:0;height:51px;line-height:51px;color:var(--white);text-decoration:none;font-family:'Cinzel',serif;font-size:17px;letter-spacing:1px;white-space:nowrap}
.nav a.active{background:var(--ink);width:110px;text-align:center}

/* hero */
.hero{left:0;top:173px;width:1200px;height:455px;background:linear-gradient(100deg,var(--teal-a),var(--teal-b))}
.hero-name{left:165px;top:258px;font-family:'Cinzel',serif;font-weight:700;font-size:56px;color:var(--white);white-space:nowrap}
.hero-qual{left:165px;top:330px;font-size:21px;color:var(--white)}
.hero-rule{left:165px;top:372px;width:122px;height:3px;background:var(--white)}
.hero-lead{left:165px;top:394px;font-size:22px;color:var(--white);white-space:nowrap}
.hero-sub{left:165px;top:434px;font-size:17px;color:var(--white)}
.btn-white{left:165px;top:478px;width:146px;height:44px;background:var(--white);color:var(--ink);font-family:'Cinzel',serif;font-weight:700;font-size:17px;display:flex;align-items:center;justify-content:center;letter-spacing:1px}
.portrait{left:705px;top:205px;width:360px;height:435px;border-radius:160px 160px 6px 6px;background:linear-gradient(180deg,#3f6f93,#2c4d72)}

/* section heads */
.head{left:0;width:1200px;text-align:center;font-family:'Cinzel',serif;font-weight:700;font-size:34px;color:var(--ink)}
.head span{color:var(--duck)}
.head-rule{left:397px;width:406px;height:1px;background:var(--line)}
.head-rule::after{content:"";position:absolute;left:178px;top:-1px;width:50px;height:3px;background:var(--duck)}

.about{left:160px;top:770px;width:880px;text-align:center;font-size:14.5px;line-height:28px}
.about p{margin-bottom:8px}
.about .q{font-weight:700;font-size:15.5px;margin-bottom:2px}
.about u{text-decoration:underline}
.btn-duck{left:527px;top:1006px;width:146px;height:44px;background:var(--duck);color:var(--white);font-family:'Cinzel',serif;font-weight:700;font-size:16px;display:flex;align-items:center;justify-content:center;letter-spacing:1px}

/* call + booking */
.callbox{left:130px;top:1102px;width:467px;height:255px;background:linear-gradient(160deg,#8aacbb,#5d8597);color:var(--white);text-align:center}
.callbox .num{position:absolute;left:0;top:120px;width:100%;font-family:'Cinzel',serif;font-size:54px;white-space:nowrap}
.bookbox{left:604px;top:1102px;width:467px;height:255px;background:var(--ink)}
.bookbox h3{position:absolute;left:0;top:32px;width:100%;text-align:center;font-family:'Cinzel',serif;font-weight:700;font-size:23px;color:var(--white);letter-spacing:1px;white-space:nowrap}
.bookbox .bar{position:absolute;left:208px;top:78px;width:52px;height:3px;background:var(--duck)}
.field{width:206px;height:43px;background:#f5f5f5;font-size:11px;color:#999;padding:0 14px;display:flex;align-items:center}
.book{width:206px;height:43px;background:var(--duck);color:var(--white);font-family:'Cinzel',serif;font-weight:700;font-size:15px;display:flex;align-items:center;justify-content:center;letter-spacing:1px}

/* testimonials */
.card{top:1495px;width:477px;height:235px;background:#fafafa;border:1px solid #e2e2e2;border-radius:4px;box-shadow:0 2px 6px rgba(0,0,0,.12);padding:28px 20px 0 20px;font-style:italic;font-size:12.5px;line-height:20.5px;color:#555}
.card .mk{font-family:Georgia,serif;font-size:40px;color:#ccc;font-style:normal;line-height:0;vertical-align:-14px;margin-right:6px}
.avatar{top:1698px;width:104px;height:104px;border-radius:50%;border:4px solid #fff;box-shadow:0 1px 5px rgba(0,0,0,.3);background:linear-gradient(160deg,#9fb5c4,#5b7487)}
.who{top:1761px;font-family:'Cinzel',serif;font-weight:700;font-size:16px;color:var(--ink);letter-spacing:1px;white-space:nowrap}
.arrow{top:1583px}

/* footer */
.footer{left:0;top:1857px;width:1200px;height:291px;background:var(--ink-soft);color:var(--white)}
.fh{top:52px;font-family:'Cinzel',serif;font-weight:700;font-size:15px;letter-spacing:.5px;white-space:nowrap}
.fh::after{content:"";position:absolute;left:0;top:30px;width:100%;height:1px;background:#555}
.links{top:90px;list-style:none;font-size:12.5px;line-height:35px}
.links li::before{content:"•";margin-right:10px;font-size:10px}
.contact{top:95px;font-size:12.5px;line-height:19px}
.contact .row{display:flex;align-items:center;gap:10px;margin-top:14px}
.map{left:537px;top:91px;width:306px;height:162px;background:linear-gradient(135deg,#cfd9bd,#b9cfe0 55%,#d8dcc4)}
.hours{top:92px;font-size:13px;line-height:29px;white-space:nowrap}
.hours .d{display:inline-block;width:105px;font-weight:700}
.bottom{left:0;top:2148px;width:1200px;height:42px;background:var(--duck);color:var(--white);font-size:12px}
</style>
</head>
<body>

<header>
  <div class="abs topline"></div>
  <div class="abs top-email">
    <svg width="16" height="12" viewBox="0 0 16 12"><rect x=".5" y=".5" width="15" height="11" fill="none" stroke="#7fa3b1"/><path d="M.5 .5 8 7 15.5 .5" fill="none" stroke="#7fa3b1"/></svg>
    info@tobenkarsh.com
  </div>
  <div class="abs top-phone">
    <svg width="16" height="16" viewBox="0 0 24 24"><path fill="#fff" d="M6.6 10.8a15 15 0 0 0 6.6 6.6l2.2-2.2c.3-.3.7-.4 1-.2 1.1.4 2.3.6 3.6.6.6 0 1 .4 1 1V20c0 .6-.4 1-1 1A17 17 0 0 1 3 4c0-.6.4-1 1-1h3.5c.6 0 1 .4 1 1 0 1.3.2 2.5.6 3.6.1.3 0 .7-.2 1z"/></svg>
    123-456-7890
  </div>
  <div class="abs pill" style="left:600px;width:230px">
    <span class="ic"><svg width="20" height="20" viewBox="0 0 20 20"><path d="M10 2v10M6 8l4 4 4-4M3 14v3h14v-3" fill="none" stroke="#fff" stroke-width="2"/></svg></span>
    Download Referral Form
  </div>
  <div class="abs pill" style="left:868px;width:232px">
    <span class="ic"><svg width="20" height="20" viewBox="0 0 20 20"><rect x="3" y="4" width="14" height="13" fill="none" stroke="#fff" stroke-width="2"/><path d="M3 8h14M7 2v4M13 2v4" stroke="#fff" stroke-width="2"/></svg></span>
    Make An Appointment
  </div>

  <nav class="abs nav">
    <a class="active" href="#" style="left:318px">HOME</a>
    <a href="#" style="left:468px">ABOUT ME</a>
    <a href="#" style="left:602px">PATIENT RESOURCES</a>
    <a href="#" style="left:825px">TESTIMONIAL</a>
    <a href="#" style="left:986px">CONTACT US</a>
  </nav>
  <div class="abs nav-logo-tab"></div>
  <div class="abs brand">TOBEN KARSH</div>
</header>

<section>
  <div class="abs hero"></div>
  <div class="abs hero-name">TOBEN KARSH</div>
  <div class="abs hero-qual">BDS (Hons) MJDF RCS (Eng)</div>
  <div class="abs hero-rule"></div>
  <div class="abs hero-lead">I am a restorative and implant dentist based in Cardiff</div>
  <div class="abs hero-sub">Nervous? Let’s see what I can do for you.</div>
  <div class="abs btn-white">ABOUT ME</div>
  <div class="abs portrait" role="img" aria-label="Portrait of the dentist in blue scrubs, arms folded on a desk"></div>
</section>

<section>
  <h2 class="abs head" style="top:683px">ABOUT <span>ME</span></h2>
  <div class="abs head-rule" style="top:745px"></div>
  <div class="abs about">
    <p class="q">BDS (Hons) MJDF RCS (Eng)</p>
    <p>I am a Severnmouth University graduate and registered with the <u>Dental Practitioners Board</u> (DPB no. 418207)</p>
    <p>I provide care for my patients at <u>Glenmorrow Dental Surgery</u>, a state of the art private practice in Glenmorrow Village, Cardiff. I have a particular interest in <u>periodontal disease</u> and in restoring missing teeth with <u>dental implants</u>.</p>
    <p>I work as a Clinical Research Fellow and a Clinical Lecturer at Westbury Dental Hospital, <u>University of Westbury</u>. My research interests include developing research methodologies, periodontal conditions, bone augmentation and peri-implant lesions, the scientific evaluation of oral health care products, toothwear, dentine hypersensitivity and tooth whitening.</p>
  </div>
  <div class="abs btn-duck">READ MORE</div>
</section>

<section>
  <div class="abs callbox">
    <svg class="abs" style="left:212px;top:60px" width="42" height="42" viewBox="0 0 24 24"><path fill="#fff" d="M6.6 10.8a15 15 0 0 0 6.6 6.6l2.2-2.2c.3-.3.7-.4 1-.2 1.1.4 2.3.6 3.6.6.6 0 1 .4 1 1V20c0 .6-.4 1-1 1A17 17 0 0 1 3 4c0-.6.4-1 1-1h3.5c.6 0 1 .4 1 1 0 1.3.2 2.5.6 3.6.1.3 0 .7-.2 1z"/></svg>
    <div class="num">123-456-7890</div>
  </div>
  <div class="abs bookbox">
    <h3>MAKE AN APPOINTMENT</h3>
    <div class="bar"></div>
    <div class="abs field" style="left:24px;top:121px">Enter Name</div>
    <div class="abs field" style="left:238px;top:121px">Enter Email</div>
    <div class="abs field" style="left:24px;top:173px">Enter Phone Number</div>
    <div class="abs book" style="left:238px;top:173px">BOOK NOW</div>
  </div>
</section>

<section>
  <h2 class="abs head" style="top:1397px">CLIENT <span>TESTIMONIAL</span></h2>
  <div class="abs head-rule" style="top:1458px"></div>

  <svg class="abs arrow" style="left:55px" width="14" height="30" viewBox="0 0 14 30"><path d="M12 2 2 15l10 13" fill="none" stroke="#ddd" stroke-width="2"/></svg>
  <svg class="abs arrow" style="left:1130px" width="14" height="30" viewBox="0 0 14 30"><path d="M2 2l10 13L2 28" fill="none" stroke="#ddd" stroke-width="2"/></svg>

  <div class="abs card" style="left:98px">
    <span class="mk">“</span>Dr Toben Karsh has been my dentist for several years now, I can quite confidently say that he is one of the most outstanding professionals I have encountered, not just in the medical world, but in all walks of life. As an international opera singer, my teeth are very important to me, both their appearance and function, and Toben’s brilliance and skill in their care is a source of great reassurance. In addition to his professional virtuosity, Toben is an exceptional person, endlessly kind, witty and interested in his patients. I am proud to give him my highest possible recommendation. <span class="mk">”</span>
  </div>
  <div class="abs avatar" style="left:128px" role="img" aria-label="Client photo"></div>
  <div class="abs who" style="left:280px">- RICHARD (LONDON)</div>

  <div class="abs card" style="left:624px">
    <span class="mk">“</span>Toben firstly is a lovely guy, that’s the first thing that strikes you, it’s not often you get treated in such a nice manner at a dentist!!<br>I am someone that has always feared the dentist for years and years and hadn’t even stepped foot in a dentist for over 5 years. From the first discussion with Toben he fully put me at ease and dispelled my fears. Toben has transformed my view of going to the dentist and also educated me along the way as to how to prevent issues in the future. <span class="mk">”</span>
  </div>
  <div class="abs avatar" style="left:652px;top:1695px" role="img" aria-label="Client photo"></div>
  <div class="abs who" style="left:802px;top:1758px">- SIMON (CARDIFF)</div>
</section>

<footer class="abs footer">
  <div class="abs fh" style="left:98px;width:122px">QUICK LINKS</div>
  <ul class="abs links" style="left:98px">
    <li>Home</li><li>About Us</li><li>Patient Resources</li><li>Testimonial</li><li>Contact Us</li>
  </ul>

  <div class="abs fh" style="left:265px;width:230px">CONTACT INFORMATION</div>
  <div class="abs contact" style="left:265px">
    <strong>Glenmorrow Dental Surgery</strong><br>41-43 Pellow Crescent, Cardiff<br>CF22 9RW
    <div class="row"><svg width="12" height="12" viewBox="0 0 24 24"><path fill="#fff" d="M6.6 10.8a15 15 0 0 0 6.6 6.6l2.2-2.2c.3-.3.7-.4 1-.2 1.1.4 2.3.6 3.6.6.6 0 1 .4 1 1V20c0 .6-.4 1-1 1A17 17 0 0 1 3 4c0-.6.4-1 1-1h3.5c.6 0 1 .4 1 1 0 1.3.2 2.5.6 3.6.1.3 0 .7-.2 1z"/></svg>123-456-7890</div>
    <div class="row"><svg width="13" height="12" viewBox="0 0 13 12"><rect x="3" y="0" width="7" height="4" fill="#fff"/><rect x="0" y="4" width="13" height="5" fill="#fff"/><rect x="3" y="7" width="7" height="5" fill="#fff"/></svg>123-456-7890</div>
    <div class="row"><svg width="13" height="10" viewBox="0 0 16 12"><rect x=".5" y=".5" width="15" height="11" fill="none" stroke="#fff"/><path d="M.5 .5 8 7 15.5 .5" fill="none" stroke="#fff"/></svg>info@tobenkarsh.com</div>
  </div>

  <div class="abs fh" style="left:540px;width:303px">LOCATION MAP</div>
  <div class="abs map" role="img" aria-label="Street map showing the practice location"></div>

  <div class="abs fh" style="left:888px;width:215px">OPENING HOURS</div>
  <div class="abs hours" style="left:890px">
    <div><span class="d">Monday :</span>8.00am - 8.00pm</div>
    <div><span class="d">Tuesday :</span>8.00am - 8.00pm</div>
    <div><span class="d">Wednesday :</span>8.00am - 8.00pm</div>
    <div><span class="d">Thursday :</span>8.00am - 8.00pm</div>
    <div><span class="d">Friday :</span>8.00am - 5.30pm</div>
    <div><span class="d">Saturday :</span>8.15am - 4.30pm</div>
  </div>
</footer>

<div class="abs bottom">
  <div class="abs" style="left:98px;top:14px">© 2017 <strong>Toben Karsh</strong>. All Rights Reserved.</div>
  <div class="abs" style="left:1073px;top:9px;width:24px;height:24px;border-radius:50%;background:var(--duck-dark)"></div>
</div>

</body>
</html>
```